New business card for civil engineering company - "Keystone Audit"

We need a business card designed for our new structural engineering company.

The company name is "Keystone Audit" logo files attached.

We would like the following:
* Two-sided card
* Simple design

Information to be placed on the card:
Name - Marcus Dellow
Job Title - Director / Structural Engineer
Credentials - BEng(Hons), CPEng, CMengNZ, IntPE(NZ)
Email - marcus.dellow@keystoneaudit.co.nz
mobile - 0219364058
website - www.keystoneaudit.co.nz

```html
<!DOCTYPE html>
<html lang="en">
<head>
<meta charset="utf-8">
<title>Keystone Audit – Business Card</title>
<link href="https://fonts.googleapis.com/css2?family=Exo+2:wght@400;600&display=swap" rel="stylesheet">
<style>
  :root {
    --backdrop: #3b3d40;
    --navy: #073c6b;
    --accent: #1c70bd;
    --sky: #7cc0e6;
    --paper: #f4f4f4;
    --ink: #2a2a2a;
    --rule: #8a8a8a;
    --white: #ffffff;
  }
  * { box-sizing: border-box; margin: 0; padding: 0; }
  html, body {
    width: 1200px; height: 1021px; overflow: hidden;
    background: var(--backdrop);
    font-family: "Exo 2", sans-serif;
  }
  .card {
    position: absolute;
    width: 680px; height: 378px;
    box-shadow: 0 18px 40px rgba(0,0,0,.45);
  }
  .card-back {
    left: 420px; top: 70px;
    background: var(--navy);
    display: flex; align-items: center; justify-content: center; gap: 18px;
  }
  .brand-mark { width: 26px; height: 26px; }
  .card-back .brand-mark { background: var(--sky); }
  .card-back .brand-name {
    color: var(--white); font-weight: 600; font-size: 40px; letter-spacing: 2px;
    text-transform: uppercase;
  }
  .card-front {
    left: 100px; top: 540px;
    background: var(--paper);
    padding: 52px 56px;
    color: var(--ink);
  }
  .person-name { color: var(--accent); font-weight: 600; font-size: 25px; }
  .person-role, .person-credentials { font-size: 17px; line-height: 1.35; }
  .divider { width: 420px; border: 0; border-top: 1.5px solid var(--rule); margin: 34px 0 30px; }
  .contact-list { list-style: none; font-size: 19px; line-height: 1.35; }
  .contact-list li { display: flex; align-items: center; gap: 9px; }
  .contact-list svg { width: 15px; height: 15px; fill: var(--accent); flex: none; }
  .front-brand {
    position: absolute; right: 48px; bottom: 44px;
    display: flex; align-items: center; gap: 12px;
  }
  .card-front .brand-mark { background: var(--accent); width: 20px; height: 20px; }
  .card-front .brand-name { color: var(--accent); font-weight: 600; font-size: 24px; }
</style>
</head>
<body>
  <section class="card card-back">
    <span class="brand-mark"></span>
    <span class="brand-name">Keystone Audit</span>
  </section>

  <section class="card card-front">
    <h1 class="person-name">Marcus Dellow</h1>
    <p class="person-role">Director / Structural Engineer</p>
    <p class="person-credentials">BEng(Hons), CPEng, CMengNZ, IntPE(NZ)</p>
    <hr class="divider">
    <ul class="contact-list">
      <li><svg viewBox="0 0 16 16"><path d="M3.5 1l2.5 3-1.5 1.6c.8 1.8 2.2 3.3 4 4.2L10 8.3l3 2.4-1.3 2.8C6.5 13.6 2.3 9.3 1.2 3.6z"/></svg>0219364058</li>
      <li><svg viewBox="0 0 16 16"><path d="M1 3h14v10H1zm1.5 1.3v.3L8 8.6l5.5-4v-.3zm0 1.8v5.6h11V6.1L8 10.2z"/></svg>marcus.dellow@keystoneaudit.co.nz</li>
      <li><svg viewBox="0 0 16 16"><path d="M8 1a7 7 0 100 14A7 7 0 008 1zm-5.4 6.3h2.5c.1-1.6.4-3 1-4a5.6 5.6 0 00-3.5 4zm0 1.4a5.6 5.6 0 003.5 4c-.6-1-.9-2.4-1-4zm3.9 0c.1 2.2.8 4 1.5 4.6.7-.6 1.4-2.4 1.5-4.6zm0-1.4h3c-.1-2.2-.8-4-1.5-4.6-.7.6-1.4 2.4-1.5 4.6zm4.4 0h2.5a5.6 5.6 0 00-3.5-4c.6 1 .9 2.4 1 4zm0 1.4c-.1 1.6-.4 3-1 4a5.6 5.6 0 003.5-4z"/></svg>www.keystoneaudit.co.nz</li>
    </ul>
    <div class="front-brand">
      <span class="brand-mark"></span>
      <span class="brand-name">Keystone Audit</span>
    </div>
  </section>
</body>
</html>
```